Business Card Design Project

We need a business card design for a new boutique consulting company, TivaConsulting. Our new logo has just been designed and we are looking for simple, clean looking business cards. Logo attached

Industry/Entity Type

Boutique

Requirements
Must have
• There must be room for each card to have the following details:
Name
Title
Address - 2 lines
Phone number
Email address
Website address

Nice to have
• May have something on the back of the buisness card - emphasing the word "Tiva".

```html
<!DOCTYPE html>
<html lang="en">
<head>
<meta charset="utf-8">
<title>TivaConsulting Business Card</title>
<link href="https://fonts.googleapis.com/css2?family=Questrial&display=swap" rel="stylesheet">
<style>
  :root {
    --page-bg: #e4e5e6;
    --card-white: #ffffff;
    --band-top: #a3a4a6;
    --band-bottom: #79797b;
    --brand-green: #8cc63f;
    --green-light: #c2e265;
    --green-dark: #72b62c;
    --text-white: #ffffff;
  }
  * { margin: 0; padding: 0; box-sizing: border-box; }
  html, body {
    width: 1099px; height: 1200px; overflow: hidden;
    background: var(--page-bg);
    font-family: "Questrial", "Century Gothic", sans-serif;
  }
  .canvas { position: relative; width: 1099px; height: 1200px; }
  .card {
    position: absolute; left: 112px; width: 877px; height: 486px;
    box-shadow: 0 1px 3px rgba(0,0,0,0.15);
    overflow: hidden;
  }
  .card--front { top: 87px; background: var(--card-white); }
  .card--back {
    top: 625px;
    background: linear-gradient(180deg, var(--green-light) 0%, var(--brand-green) 55%, var(--green-dark) 100%);
  }
  .brand {
    position: absolute; left: 58px; top: 108px;
    display: flex; align-items: center; gap: 16px;
  }
  .brand__mark { width: 24px; height: 24px; background: var(--brand-green); }
  .brand__name { font-size: 72px; line-height: 1; color: var(--brand-green); letter-spacing: -1px; }
  .info-band {
    position: absolute; left: 0; top: 203px; width: 100%; height: 283px;
    background: linear-gradient(180deg, var(--band-top), var(--band-bottom));
    color: var(--text-white);
  }
  .person { position: absolute; left: 58px; top: 114px; }
  .person__name { font-size: 35px; line-height: 1.25; }
  .person__title { font-size: 31px; line-height: 1.3; }
  .divider {
    position: absolute; left: 501px; top: 83px; width: 2px; height: 145px;
    background: var(--text-white);
  }
  .contact {
    position: absolute; left: 532px; top: 84px;
    font-style: normal; font-size: 22.5px; line-height: 29px;
  }
  .contact strong { font-weight: 700; }
  .flight-art {
    position: absolute; left: 0; top: 50px; width: 720px; height: 436px;
    background: radial-gradient(ellipse at 70% 20%, rgba(255,255,255,0.22) 0%, rgba(255,255,255,0.08) 45%, rgba(255,255,255,0) 75%);
  }
  .back-wordmark {
    position: absolute; left: 56px; top: 376px;
    display: flex; align-items: center; gap: 48px;
    color: rgba(255,255,255,0.55);
  }
  .back-wordmark__mark { width: 34px; height: 34px; background: rgba(255,255,255,0.55); }
  .back-wordmark__name { font-size: 108px; line-height: 1; letter-spacing: -2px; }
</style>
</head>
<body>
<main class="canvas">
  <section class="card card--front">
    <div class="brand">
      <span class="brand__mark"></span>
      <span class="brand__name">TivaConsulting</span>
    </div>
    <div class="info-band">
      <div class="person">
        <p class="person__name">Daniel Hart</p>
        <p class="person__title">Managing Director</p>
      </div>
      <span class="divider"></span>
      <address class="contact">
        4120, Marlowe Ave.<br>
        Los Angeles, CA<br>
        ph.: <strong>310 555 0142</strong><br>
        inbox@tiva.com<br>
        www.tivaconsulting.com
      </address>
    </div>
  </section>

  <section class="card card--back">
    <div class="flight-art" role="img" aria-label="Illustration of a golf ball's flight arc toward a flag"></div>
    <div class="back-wordmark">
      <span class="back-wordmark__mark"></span>
      <span class="back-wordmark__name">TivaConsulting</span>
    </div>
  </section>
</main>
</body>
</html>
```